We are launching in December, a range of supplements and vitamins.

We have just made an amend to the mission statement and how we are going to give back to society. Please can you add both to the packaging:

Verdant’s purpose is to support health, wellbeing and longevity, so that we can all thrive in the modern world; an environment so alien to that in which we evolved. Embracing technology, research and science, we harness nature’s goodness - enabling us all to love life – naturally.

Twice Kind Promise. For each and every Verdant supplement you take, we provide a supplement to an under nourished child.

For every supplement we sell: £1 goes to the charity ‘Little Lights Fund’ and in addition we provide one healthy meal to an under privileged child in India.

My name is Mark Holloway and I own several companies including www.quartzelle.com (you can check me out on Infopedex – I am not the football referee nor the rocket scientist, but the entrepreneur) . Over the past 2 years I have been writing a book to help people live more healthily and it launches in December. It’s called Verdant Way. While doing my research for the book, I came to realise that most supplements and vitamin products on the market are rubbish! Most are made for profit and not for the benefit of the consumer. I want to change all of that. Howard Pellow is patron of a charity I set up with my brother Paul Holloway and together we have built 11 schools in Asia. I am hoping to get Howards help in getting my supplements to market.

Positioning of our supplements - In a world where so much has changed from the one our bodies were designed to thrive, at Verdant Supplements we are driven by one purpose; to globally provide healthy support to life in the 21st century. While the roots of our wellbeing supplements date back beyond 10,000BC, we embrace modern technology and science, to encapsulate powerful phytonutrients, herbs and other goodness. The essence of which is to promote health, happiness and longevity.

So what are we looking for in the design? Something that stands out. Something that looks professional. A design and concept that can role out across 24 different products. Some products are simple, just one ingredient, such as vitamin D3, Magnesium, Garlic Extracts etc, and others are our own formulas where there are up to 30 different ingredients. You can contact me at any time with questions at Mark@verdantway-example.com

Target Market(s)

Male & Female 20 years plus, mainly UK

Industry/Entity Type

Medical

Logo Text

VERDANT - Sub heading = Thriving Days Gently

Colors

Designer to choose colors to be used in the design.

Requirements
Must have
• see attached powerpoint.
• We have just made an amend to the mission statement and how we are going to give back to society. Please can you add both to the packaging:
• Verdant’s purpose is to support health, wellbeing and longevity, so that we can all thrive in the modern world; an environment so alien to that in which we evolved. Embracing technology, research and science, we harness nature’s goodness - enabling us all to love life – naturally.
• Twice Kind Promise. For each and every Verdant supplement you take, we provide a supplement to an under nourished child.
Nice to have
• see attached powerpoint
Should not have
• see attached powerpoint

```html
<!DOCTYPE html>
<html lang="en">
<head>
<meta charset="utf-8">
<title>Verdant Energy – Packaging</title>
<link rel="stylesheet" href="https://fonts.googleapis.com/css2?family=Oswald:wght@500;700&family=Patrick+Hand&display=swap">
<style>
  :root {
    --kraft: #e6d5b6;
    --kraft-dark: #d9c6a3;
    --teal: #2e9a86;
    --teal-dark: #237a6a;
    --red: #e0231f;
    --ink: #1c1c1c;
    --white: #ffffff;
    --stage: #eef1ea;
    --meadow: #3f9a82;
  }
  * { box-sizing: border-box; margin: 0; padding: 0; }
  html, body { width: 1200px; height: 1000px; overflow: hidden; }
  body { background: var(--stage); font-family: "Patrick Hand", cursive; color: var(--ink); position: relative; }

  .carton { position: absolute; left: 96px; top: 100px; display: flex; height: 800px; box-shadow: 0 14px 30px rgba(0,0,0,.12); }

  /* Side panel */
  .side-panel { width: 104px; background: var(--kraft-dark); display: flex; flex-direction: column; align-items: center; padding-top: 12px; position: relative; font-family: Arial, sans-serif; }
  .side-panel .heart-badge { width: 22px; height: 22px; flex: none; }
  .side-heading { font-size: 8.5px; font-weight: 700; text-transform: uppercase; margin-top: 6px; text-align: center; }
  .side-text { font-size: 7.6px; line-height: 1.2; text-align: center; padding: 3px 7px 0; }
  .side-mascot { width: 30px; height: 40px; margin-top: 8px; border-radius: 10px; background: linear-gradient(#f2c531, #dca71c); flex: none; }
  .side-mission { margin: 8px 7px 0; font-size: 7.6px; line-height: 1.2; text-align: center; }
  .side-disclaimer { margin: 8px 7px 0; border: 1px solid var(--ink); padding: 4px; font-size: 7px; line-height: 1.2; }
  .side-origin { margin-top: 8px; font-size: 8.5px; font-weight: 700; text-align: center; line-height: 1.2; }
  .side-footer { position: absolute; bottom: 0; left: 0; right: 0; height: 100px; background: var(--teal); color: var(--white); font-size: 8.5px; text-align: center; padding: 14px 8px; line-height: 1.2; }
  .side-footer svg { width: 18px; height: 18px; margin-top: 6px; }

  /* Label shared */
  .label { background: var(--kraft); position: relative; overflow: hidden; text-align: center; }
  .brand-tab { background: var(--teal); color: var(--white); margin: 0 auto; border-radius: 0 0 14px 14px; display: flex; flex-direction: column; align-items: center; justify-content: center; }
  .brand-name { font-family: Oswald, sans-serif; font-weight: 700; letter-spacing: 4px; line-height: 1; }
  .brand-tagline { font-family: Oswald, sans-serif; font-weight: 500; text-transform: uppercase; line-height: 1.1; }
  .product-title { font-family: Oswald, sans-serif; font-weight: 700; color: var(--ink); line-height: 1; letter-spacing: 1px; white-space: nowrap; }
  .claim { font-family: Oswald, sans-serif; font-weight: 500; color: var(--teal); display: inline-flex; align-items: center; gap: 8px; }
  .claim svg { width: 18px; height: 18px; }
  .features p { line-height: 1.3; }
  .meadow { position: absolute; left: 0; right: 0; background: linear-gradient(to bottom, rgba(63,154,130,0) 0%, rgba(63,154,130,.55) 55%, var(--meadow) 100%); }
  .guarantee { position: absolute; left: 0; right: 0; bottom: 0; background: var(--teal); color: var(--white); display: flex; align-items: center; justify-content: center; gap: 14px; font-family: Oswald, sans-serif; font-weight: 500; text-transform: uppercase; line-height: 1.15; }
  .heart-badge { flex: none; }

  /* Carton front */
  .front-panel { width: 480px; height: 800px; }
  .front-panel .brand-tab { width: 280px; height: 118px; }
  .front-panel .brand-name { font-size: 50px; }
  .front-panel .brand-tagline { font-size: 17px; margin-top: 4px; }
  .front-panel .product-title { font-size: 58px; margin-top: 30px; }
  .front-panel .claim { font-size: 19px; margin-top: 18px; }
  .front-panel .features { font-size: 17px; margin: 16px 60px 0; }
  .front-panel .features p + p { margin-top: 10px; }
  .count-pill { display: inline-block; background: var(--ink); color: var(--white); font-family: Oswald, sans-serif; font-weight: 700; font-size: 22px; padding: 4px 26px; border-radius: 6px; margin-top: 26px; }
  .free-from { display: flex; justify-content: center; gap: 14px; margin-top: 16px; font-family: Oswald, sans-serif; font-weight: 500; font-size: 15px; }
  .free-from span { display: inline-flex; align-items: center; gap: 4px; }
  .free-from svg { width: 16px; height: 16px; }
  .front-panel .meadow { top: 610px; height: 90px; }
  .front-panel .guarantee { height: 100px; font-size: 17px; }
  .front-panel .heart-badge { width: 30px; height: 30px; }

  /* Bottle label */
  .bottle-label { position: absolute; left: 700px; top: 270px; width: 400px; height: 480px; box-shadow: 0 14px 30px rgba(0,0,0,.12); }
  .bottle-label .brand-tab { width: 230px; height: 96px; margin-left: 60px; }
  .bottle-label .brand-name { font-size: 40px; }
  .bottle-label .brand-tagline { font-size: 14px; margin-top: 3px; }
  .tablet-badge { position: absolute; right: 44px; top: 30px; width: 46px; height: 46px; border-radius: 50%; background: var(--ink); color: var(--white); border: 2px solid var(--kraft); outline: 2px solid var(--ink); font-family: Oswald, sans-serif; font-weight: 700; display: flex; flex-direction: column; align-items: center; justify-content: center; line-height: 1; font-size: 16px; }
  .tablet-badge small { font-size: 6px; letter-spacing: .5px; }
  .bottle-label .product-title { font-size: 48px; margin-top: 22px; }
  .bottle-label .claim { font-size: 16px; margin-top: 12px; }
  .bottle-label .features { font-size: 15px; margin: 14px 40px 0; }
  .bottle-label .features p + p { margin-top: 8px; }
  .bottle-label .meadow { top: 338px; height: 70px; }
  .bottle-label .guarantee { height: 74px; font-size: 14px; }
  .bottle-label .heart-badge { width: 22px; height: 22px; }
</style>
</head>
<body>
<svg width="0" height="0" style="position:absolute">
  <defs>
    <symbol id="heart-badge" viewBox="0 0 30 30">
      <circle cx="15" cy="15" r="14" fill="#e0231f" stroke="#fff" stroke-width="1.5"/>
      <path d="M15 22 L8.5 15.5 A3.6 3.6 0 0 1 15 10.5 A3.6 3.6 0 0 1 21.5 15.5 Z" fill="#fff"/>
    </symbol>
    <symbol id="tick" viewBox="0 0 16 16">
      <path d="M2 9 L6 13 L14 2" fill="none" stroke="#e0231f" stroke-width="2.6" stroke-linecap="round" stroke-linejoin="round"/>
    </symbol>
    <symbol id="burst-left" viewBox="0 0 18 18">
      <path d="M2 4 L12 7 M1 10 L13 10 M2 16 L12 13" stroke="#e0231f" stroke-width="2" stroke-linecap="round"/>
    </symbol>
    <symbol id="burst-right" viewBox="0 0 18 18">
      <path d="M16 4 L6 7 M17 10 L5 10 M16 16 L6 13" stroke="#e0231f" stroke-width="2" stroke-linecap="round"/>
    </symbol>
  </defs>
</svg>

<div class="carton">
  <aside class="side-panel">
    <svg class="heart-badge"><use href="#heart-badge"/></svg>
    <p class="side-heading">Twice Kind Promise</p>
    <p class="side-text">For each and every Verdant supplement you take, we provide a supplement to an under nourished child.</p>
    <p class="side-text">For every supplement we sell: £1 goes to the charity ‘Little Lights Fund’ and in addition we provide one healthy meal to an under privileged child in India.</p>
    <div class="side-mascot" role="img" aria-label="Charity mascot illustration"></div>
    <p class="side-mission">Verdant’s purpose is to support health, wellbeing and longevity, so that we can all thrive in the modern world; an environment so alien to that in which we evolved. Embracing technology, research and science, we harness nature’s goodness – enabling us all to love life – naturally.</p>
    <p class="side-disclaimer">*These statements have not been evaluated by the Supplement Standards Board. This product is not intended to diagnose, treat, cure or prevent any disease.</p>
    <p class="side-origin">MADE IN<br>GREAT BRITAIN</p>
    <div class="side-footer">
      Packaging BPA Free. Please dispose responsibly.
      <svg viewBox="0 0 20 20"><path d="M10 3 L14 9 M10 3 L6 9 M4 13 L16 13 M16 13 L13 8 M4 13 L7 8" fill="none" stroke="#fff" stroke-width="1.6" stroke-linecap="round"/></svg>
    </div>
  </aside>

  <section class="label front-panel">
    <div class="brand-tab">
      <span class="brand-name">VERDANT</span>
      <span class="brand-tagline">Thriving Days Gently</span>
    </div>
    <h1 class="product-title">VERDANT ENERGY</h1>
    <div class="claim"><svg><use href="#burst-left"/></svg>EXTRACTING NATURES GREATNESS<svg><use href="#burst-right"/></svg></div>
    <div class="features">
      <p>Vitamins from the B-Complex suppport<br>100% to 400% NRV</p>
      <p>Includes Maca Extract, CoQ10, Alpha Lipoic Acid<br>and Cinnamon Bark Extract</p>
      <p>Loaded with ingredients contributing to normal energy yielding metabolism</p>
      <p>Vitamin D3 provided at an exceptional 1000iu</p>
    </div>
    <div class="count-pill">30 TABLETS</div>
    <div class="free-from">
      <span><svg><use href="#tick"/></svg>No Added Colouring</span>
      <span><svg><use href="#tick"/></svg>No Added Sugar</span>
      <span><svg><use href="#tick"/></svg>No Gluten</span>
    </div>
    <div class="meadow" role="img" aria-label="Meadow silhouette with ferns, flowers and butterflies"></div>
    <div class="guarantee">
      <svg class="heart-badge"><use href="#heart-badge"/></svg>
      <span>Love the difference in 30 days,<br>or get 100% of your money back</span>
      <svg class="heart-badge"><use href="#heart-badge"/></svg>
    </div>
  </section>
</div>

<section class="label bottle-label">
  <div class="brand-tab">
    <span class="brand-name">VERDANT</span>
    <span class="brand-tagline">Thriving Days Gently</span>
  </div>
  <div class="tablet-badge">30<small>TABLETS</small></div>
  <h2 class="product-title">VERDANT ENERGY</h2>
  <div class="claim"><svg><use href="#burst-left"/></svg>EXTRACTING NATURES GREATNESS<svg><use href="#burst-right"/></svg></div>
  <div class="features">
    <p>Vitamins from the B-Complex suppport<br>100% to 400% NRV</p>
    <p>Includes Maca Extract, CoQ10, Alpha Lipoic Acid<br>and Cinnamon Bark Extract</p>
  </div>
  <div class="meadow" role="img" aria-label="Meadow silhouette with ferns, flowers and butterflies"></div>
  <div class="guarantee">
    <svg class="heart-badge"><use href="#heart-badge"/></svg>
    <span>Love the difference in 30 days,<br>or get 100% of your money back</span>
    <svg class="heart-badge"><use href="#heart-badge"/></svg>
  </div>
</section>
</body>
</html>
```